Mixed Martial Arts gym that is known for high quality athletes, students and training

We need a business card designed that is unique and stands out. Something that is not so dark and boring but looks 'energetic' to those that are given it. The customers that would receive this card would be looking to sign up for martial arts or fitness training and this card is used for corporate sponsorships and networking as well.

Marcus Pellow-Grant
0417305962 or 0409561738
Level 1, 284 Wendover Road. Carrowvale NSW 2781
marcus@kinetiqcombatworks.com.au
www.kinetiqcombatworks.com

```html
<!DOCTYPE html>
<html lang="en">
<head>
<meta charset="utf-8">
<title>Kinetiq Combat Works – Business Card</title>
<link rel="stylesheet" href="https://fonts.googleapis.com/css2?family=Exo+2:wght@500;600&family=Questrial&display=swap">
<style>
  :root {
    --backdrop: #5c5c5c;
    --paper: #ffffff;
    --charcoal: #353132;
    --orange: #f7941d;
    --ink: #2b2b2b;
    --muted: #5a5a5a;
    --contact: #e9e9e9;
  }
  * { box-sizing: border-box; margin: 0; padding: 0; }
  html, body {
    width: 1136px;
    height: 1200px;
    overflow: hidden;
    background: var(--backdrop);
  }
  .business-card {
    position: absolute;
    left: 88px;
    top: 305px;
    width: 960px;
    height: 590px;
    background: var(--paper);
    box-shadow: 0 6px 18px rgba(0,0,0,0.35);
    overflow: hidden;
  }
  .card-header {
    position: absolute;
    left: 0; top: 0;
    width: 100%;
    height: 264px;
    background: var(--paper);
  }
  .brand {
    position: absolute;
    left: 72px;
    top: 108px;
    display: flex;
    align-items: center;
    gap: 14px;
    font-family: "Exo 2", sans-serif;
    font-weight: 600;
    font-size: 44px;
    color: var(--orange);
    letter-spacing: 0.5px;
  }
  .brand-mark {
    width: 28px;
    height: 28px;
    background: var(--orange);
  }
  .holder {
    position: absolute;
    left: 500px;
    top: 40px;
  }
  .holder-name {
    font-family: "Exo 2", sans-serif;
    font-weight: 500;
    font-size: 40px;
    color: var(--ink);
    line-height: 1.1;
  }
  .holder-role {
    font-family: "Questrial", sans-serif;
    font-size: 26px;
    color: var(--muted);
    margin-top: 6px;
  }
  .card-body {
    position: absolute;
    left: 0; top: 264px;
    width: 100%;
    height: 326px;
    background: var(--charcoal);
  }
  .accent-band {
    position: absolute;
    inset: 0;
    background: var(--orange);
    clip-path: polygon(83% 0, 100% 0, 100% 100%, 64.5% 100%);
  }
  .contact-list {
    position: absolute;
    left: 72px;
    top: 46px;
    list-style: none;
    font-family: "Questrial", sans-serif;
    font-size: 26px;
    color: var(--contact);
    line-height: 34.5px;
  }
  .contact-list li {
    display: flex;
    align-items: center;
    gap: 12px;
  }
  .icon {
    width: 20px;
    height: 20px;
    flex: none;
    fill: var(--orange);
    stroke: var(--orange);
  }
</style>
</head>
<body>
  <article class="business-card">
    <header class="card-header">
      <div class="brand">
        <span class="brand-mark"></span>
        <span class="brand-name">Team Kinetiq</span>
      </div>
      <div class="holder">
        <h1 class="holder-name">Marcus Pellow-Grant</h1>
        <p class="holder-role">Managing Director</p>
      </div>
    </header>
    <section class="card-body">
      <div class="accent-band"></div>
      <ul class="contact-list">
        <li>
          <svg class="icon" viewBox="0 0 20 20"><path stroke="none" d="M6 2c1 0 2 3 2 4s-2 1-2 2c0 2 3 5 5 6 1 0 1-2 2-2s4 1 4 2-2 4-4 4C8 18 2 11 2 6c0-2 3-4 4-4z"/></svg>
          <span>0409561738</span>
        </li>
        <li>
          <svg class="icon" viewBox="0 0 20 20"><path stroke="none" d="M6 2c1 0 2 3 2 4s-2 1-2 2c0 2 3 5 5 6 1 0 1-2 2-2s4 1 4 2-2 4-4 4C8 18 2 11 2 6c0-2 3-4 4-4z"/></svg>
          <span>0417305962</span>
        </li>
        <li>
          <svg class="icon" viewBox="0 0 20 20"><rect x="2" y="5" width="16" height="11" fill="none" stroke-width="2"/><path d="M2 5l8 6 8-6" fill="none" stroke-width="2"/></svg>
          <span>marcus@kinetiqcombatworks.com.au</span>
        </li>
        <li>
          <svg class="icon" viewBox="0 0 20 20" fill="none"><circle cx="10" cy="10" r="8" fill="none" stroke-width="1.8"/><ellipse cx="10" cy="10" rx="3.5" ry="8" fill="none" stroke-width="1.5"/><path d="M2 10h16M4 6h12M4 14h12" stroke-width="1.3"/></svg>
          <span>www.kinetiqcombatworks.com</span>
        </li>
        <li class="address">Level 1, 284 Wendover Road.</li>
        <li class="address">Carrowvale NSW 2781</li>
      </ul>
    </section>
  </article>
</body>
</html>
```